Graphic Design Project

I need to create a graphic design, which needs to be editable for me in Powerpoint... I have attached it a draft of it, but I need to be able to change the text of it. I want it to look more professional
Updates

Target Market(s)

Business Executives

Industry/Entity Type

Graphic Design

Requirements
Must have
• Make it look professional; the colors can change; I just need to be able to edit the text in powerpoint or either word

```html
<!DOCTYPE html>
<html lang="en">
<head>
<meta charset="utf-8">
<title>IT Transformation Pyramid</title>
<link rel="stylesheet" href="https://fonts.googleapis.com/css2?family=Libre+Baskerville:wght@700&family=Carlito:wght@700&display=swap">
<style>
  :root {
    --page: #ffffff;
    --ink: #1c1a24;
    --headline: #e8141c;
    --stone-light: #f4f2ef;
    --stone-mid: #dcd8d2;
    --stone-edge: #c9c4bc;
    --red-light: #f9d2c4;
    --red-deep: #dd3417;
    --purple-light: #cbbde6;
    --purple-deep: #3a2770;
    --yellow-light: #fdf7a6;
    --yellow-deep: #f4e600;
    --orange-light: #fddcb3;
    --orange-deep: #ef8a1e;
    --pink-light: #fbd5e6;
    --pink-deep: #e5237e;
    --green-light: #d9ecd3;
    --green-deep: #2f8a3d;
    --coral-light: #fbd0bd;
    --coral-deep: #e64420;
  }
  html, body {
    margin: 0;
    padding: 0;
    width: 1200px;
    height: 900px;
    overflow: hidden;
    background: var(--page);
  }
  .pyramid {
    display: block;
    width: 1200px;
    height: 900px;
  }
  .stone { fill: url(#stoneFill); stroke: var(--stone-edge); stroke-width: 1; }
  .block { stroke: rgba(40, 30, 40, 0.55); stroke-width: 1; filter: drop-shadow(1px 2px 2px rgba(0,0,0,0.35)); }
  .block--red { fill: url(#redFill); }
  .block--purple { fill: url(#purpleFill); }
  .block--yellow { fill: url(#yellowFill); }
  .block--orange { fill: url(#orangeFill); }
  .block--pink { fill: url(#pinkFill); }
  .block--green { fill: url(#greenFill); }
  .block--coral { fill: url(#coralFill); }

  .s-stone-light { stop-color: var(--stone-light); }
  .s-stone-mid { stop-color: var(--stone-mid); }
  .s-red-light { stop-color: var(--red-light); }
  .s-red-deep { stop-color: var(--red-deep); }
  .s-purple-light { stop-color: var(--purple-light); }
  .s-purple-deep { stop-color: var(--purple-deep); }
  .s-yellow-light { stop-color: var(--yellow-light); }
  .s-yellow-deep { stop-color: var(--yellow-deep); }
  .s-orange-light { stop-color: var(--orange-light); }
  .s-orange-deep { stop-color: var(--orange-deep); }
  .s-pink-light { stop-color: var(--pink-light); }
  .s-pink-deep { stop-color: var(--pink-deep); }
  .s-green-light { stop-color: var(--green-light); }
  .s-green-deep { stop-color: var(--green-deep); }
  .s-coral-light { stop-color: var(--coral-light); }
  .s-coral-deep { stop-color: var(--coral-deep); }

  .label {
    font-family: "Libre Baskerville", "Book Antiqua", Georgia, serif;
    font-weight: 700;
    font-size: 12.5px;
    fill: var(--ink);
  }
  .label--apex { font-size: 12px; letter-spacing: 0.2px; }
  .headline {
    font-family: "Carlito", Calibri, Arial, sans-serif;
    font-weight: 700;
    font-size: 29px;
    letter-spacing: 1px;
    fill: var(--headline);
  }
</style>
</head>
<body>
<svg class="pyramid" viewBox="0 0 960 720" xmlns="http://www.w3.org/2000/svg" role="img" aria-label="IT transformation pyramid built on managing change">
  <defs>
    <linearGradient id="stoneFill" x1="0" y1="0" x2="0" y2="1">
      <stop offset="0" class="s-stone-mid"/>
      <stop offset="0.75" class="s-stone-mid"/>
      <stop offset="1" class="s-stone-light"/>
    </linearGradient>
    <linearGradient id="redFill" x1="0" y1="0" x2="0" y2="1">
      <stop offset="0" class="s-red-light"/><stop offset="1" class="s-red-deep"/>
    </linearGradient>
    <linearGradient id="purpleFill" x1="1" y1="0" x2="0" y2="1">
      <stop offset="0" class="s-purple-light"/><stop offset="0.85" class="s-purple-deep"/>
    </linearGradient>
    <linearGradient id="yellowFill" x1="0" y1="0" x2="1" y2="1">
      <stop offset="0" class="s-yellow-light"/><stop offset="0.8" class="s-yellow-deep"/>
    </linearGradient>
    <linearGradient id="orangeFill" x1="1" y1="0" x2="0" y2="1">
      <stop offset="0" class="s-orange-light"/><stop offset="0.9" class="s-orange-deep"/>
    </linearGradient>
    <linearGradient id="pinkFill" x1="0" y1="0" x2="0" y2="1">
      <stop offset="0" class="s-pink-light"/><stop offset="1" class="s-pink-deep"/>
    </linearGradient>
    <linearGradient id="greenFill" x1="0" y1="0" x2="0" y2="1">
      <stop offset="0" class="s-green-light"/><stop offset="1" class="s-green-deep"/>
    </linearGradient>
    <linearGradient id="coralFill" x1="0" y1="0" x2="0" y2="1">
      <stop offset="0" class="s-coral-light"/><stop offset="1" class="s-coral-deep"/>
    </linearGradient>
  </defs>

  <g class="foundation">
    <path class="stone" d="M478 14 L905 490 L818 597 L138 597 L48 490 Z"/>
    <text class="headline" x="490" y="551" text-anchor="middle">MANAGING CHANGE</text>
  </g>

  <g class="tier tier--apex">
    <path class="block block--red" d="M478 44 L578 172 L376 172 Z"/>
    <text class="label label--apex" x="478" y="140" text-anchor="middle">IT VISION &amp;</text>
    <text class="label label--apex" x="478" y="160" text-anchor="middle">LEADERSHIP</text>
  </g>

  <g class="tier tier--two">
    <path class="block block--purple" d="M372 178 L474 178 L474 277 L272 277 Z"/>
    <text class="label" x="465" y="208" text-anchor="end">Maintain IT</text>
    <text class="label" x="465" y="228" text-anchor="end">Operational</text>
    <text class="label" x="465" y="248" text-anchor="end">Excellence</text>

    <path class="block block--yellow" d="M481 178 L581 178 L680 277 L481 277 Z"/>
    <text class="label" x="490" y="221">Create Business</text>
    <text class="label" x="490" y="241">Value</text>
  </g>

  <g class="tier tier--three">
    <path class="block block--orange" d="M266 283 L369 283 L369 382 L168 382 Z"/>
    <text class="label" x="357" y="340" text-anchor="end">Transform IT Team</text>

    <path class="block block--pink" d="M378 283 L578 283 L578 382 L378 382 Z"/>
    <text class="label" x="478" y="327" text-anchor="middle">Master Relationship</text>
    <text class="label" x="478" y="347" text-anchor="middle">Management</text>

    <path class="block block--green" d="M586 283 L690 283 L786 382 L586 382 Z"/>
    <text class="label" x="596" y="327">Market &amp;</text>
    <text class="label" x="596" y="347">Communicate Value</text>
  </g>

  <g class="tier tier--base">
    <path class="block block--green" d="M160 389 L264 389 L264 488 L60 488 Z"/>
    <text class="label" x="255" y="432" text-anchor="end">Customer</text>
    <text class="label" x="255" y="451" text-anchor="end">Engagement Model</text>

    <path class="block block--coral" d="M273 389 L473 389 L473 488 L273 488 Z"/>
    <text class="label" x="372" y="431" text-anchor="middle">Service-Minded</text>
    <text class="label" x="372" y="450" text-anchor="middle">IT Culture</text>

    <path class="block block--purple" d="M483 389 L683 389 L683 488 L483 488 Z"/>
    <text class="label" x="582" y="431" text-anchor="middle">Policy, Process &amp;</text>
    <text class="label" x="582" y="450" text-anchor="middle">Methodologies</text>

    <path class="block block--pink" d="M693 389 L791 389 L891 488 L693 488 Z"/>
    <text class="label" x="767" y="444" text-anchor="middle">Meaningful Metrics</text>
  </g>
</svg>
</body>
</html>
```